E-commerce Website - new look and feel

Link to website
http://198.51.100.42/~brontava/brontavale_ecommerce/index.php#

Home page
-Header
- -Search bar and add to cart
-Drop down - Multi layer category representation: 1st main category level in menu bar style, 2nd category to follow and 3rd category
-Banner
-Footer

-Search listing

Category page
-Product listing
-

Product detail page
-Product variation tabular view
-

Checkout page
-

404 link/product image not found
Should be fun and engaging customers

Recent search products/ preferred products for customers

all pages:
Headroom js search bar once you are lower down the page

Shrinking navbar

Target Market(s)

Telecommunication installers, electricians working on Industrial plants and projects, on the move customers that need immediate products, procurement officers buying for projects, hard to get items customers, Car hobbyists ( future market ) for some specific product like stainless steel braid(sleeve)

Industry/Entity Type

Telecommunications

Number of Pages Required

5+ page

Colors

Designer to choose colors to be used in the design.

Requirements
Must have
• - less cluttered design
• - Easy to navigate
• - more white area on all pages
• - quick orders
• - repetitive product ordering by customers menu/list
• - branding consistency, logo colours and design
Nice to have
• -modern look
• -user friendly for less technical and computer skilled customers
• -quick to navigate
• - fun text to make customer feel at ease when navigating through website
Should not have
• -too much details
• -

```html
<!DOCTYPE html>
<html lang="en">
<head>
<meta charset="utf-8">
<title>Brontavale Asia Pacific – Home</title>
<link href="https://fonts.googleapis.com/css2?family=Montserrat:wght@500;600;700;800&family=Open+Sans:wght@400;600;700;800&display=swap" rel="stylesheet">
<style>
:root{
  --navy:#0d5aa7;
  --sky:#1a95e8;
  --ink:#222;
  --muted:#555;
  --card:#f8f6f6;
  --line:#e2e2e2;
  --white:#fff;
  --arrow:#8a8a8a;
}
*{box-sizing:border-box;margin:0;padding:0}
html,body{width:1200px;height:2628px;overflow:hidden;background:var(--white);font-family:"Open Sans",sans-serif;color:var(--ink)}
.page{position:relative;width:1200px;height:2628px}
.abs{position:absolute}
.btn{display:flex;align-items:center;justify-content:center;background:var(--navy);color:var(--white);font-family:"Montserrat",sans-serif;font-weight:700;border-radius:3px}

/* header */
.brand{left:131px;top:28px;display:flex;align-items:center;gap:14px}
.brand-dot{width:46px;height:46px;border-radius:50%;background:var(--sky)}
.brand-name{font-family:"Montserrat",sans-serif;font-weight:800;font-size:28px;color:#333;line-height:1.05}
.brand-name small{display:block;font-size:13px;letter-spacing:2px}
.top-mail{left:782px;top:19px;font-size:11.5px;color:#333;display:flex;align-items:center;gap:8px}
.login{left:1000px;top:17px;width:65px;height:25px;font-size:10px}
.search{left:485px;top:61px;width:417px;height:37px;border:1px solid #cfcfcf;border-radius:4px;display:flex;font-size:10.5px}
.search .cat{width:110px;border-right:1px solid #cfcfcf;display:flex;align-items:center;padding-left:12px;gap:6px}
.search .field{flex:1;display:flex;align-items:center;padding-left:16px}
.search .go{width:34px;background:var(--sky);border-radius:0 4px 4px 0;display:flex;align-items:center;justify-content:center}
.call{left:922px;top:62px;display:flex;gap:10px;align-items:center}
.call p{font-size:9.5px;color:#333}
.call strong{display:block;font-size:19px;font-weight:400;color:#333}
.nav{top:126px;font-family:"Montserrat",sans-serif;font-weight:700;font-size:12.5px;color:#333}
.cart{left:980px;top:120px;font-family:"Montserrat",sans-serif;font-size:10px;font-weight:700;line-height:1.2}
.cart span{color:var(--sky);font-size:12px}

/* hero */
.hero{left:0;top:166px;width:1200px;height:528px;background:linear-gradient(120deg,#c23a2e 0%,#2a7a3a 22%,#2d6ac8 38%,#2a2a2e 55%,#5c5c60 80%,#6a6a6e 100%)}
.hero-title{left:793px;top:320px;font-family:"Open Sans",sans-serif;font-weight:700;font-size:50px;color:var(--white)}
.hero-text{left:795px;top:388px;width:320px;font-size:14.5px;color:var(--white);line-height:1.35}
.hero-btn{left:795px;top:452px;width:137px;height:37px;background:var(--sky);font-size:17px;font-family:"Open Sans",sans-serif}
.dots{left:556px;top:635px;display:flex;gap:13px}
.dots i{width:11px;height:11px;border-radius:50%;background:var(--white);display:block}
.dots i.on{background:var(--sky);box-shadow:0 0 0 2px var(--white)}

/* sections */
.sec-title{left:0;width:1200px;text-align:center;font-family:"Open Sans",sans-serif;font-weight:800;font-size:24px;color:var(--navy)}
.sec-sub{left:0;width:1200px;text-align:center;font-size:14px;color:var(--muted)}
.grid{left:124px;top:892px;width:948px;display:grid;grid-template-columns:repeat(4,231px);gap:8px 8px}
.card{height:294px;background:var(--card);border:1px solid var(--line);text-align:center;padding-top:26px;position:relative}
.card h3{font-size:18px;font-weight:700;line-height:1.3}
.card h3 span{display:block;font-weight:400}
.card .btn{width:76px;height:25px;font-size:9px;margin:14px auto 0}
.card .photo{position:absolute;left:22px;right:22px;bottom:22px;height:120px;border-radius:4px}
.more{left:522px;top:1543px;width:154px;height:39px;background:var(--sky);font-family:"Open Sans",sans-serif;font-size:14px}
.band{left:0;top:1660px;width:1200px;height:18px;background:linear-gradient(#fff,#f0f0f0)}

.product{width:240px;text-align:center}
.product .photo{height:132px;margin:0 auto;width:220px;border-radius:6px}
.product p{font-size:13px;margin-top:50px}
.product .price{font-size:20px;margin-top:8px}
.product .price sup{font-size:11px}
.product .btn{width:90px;height:24px;font-size:9px;margin:10px auto 0}
.arrow{top:1945px;width:28px;height:32px;background:var(--arrow);display:flex;align-items:center;justify-content:center}

/* footer */
.footer{left:0;top:2237px;width:1200px;height:391px;background:var(--sky);color:var(--white)}
.f-brand{left:120px;top:112px;font-family:"Montserrat",sans-serif;font-weight:800;font-size:26px;display:flex;align-items:center;gap:12px}
.f-brand i{width:40px;height:40px;border-radius:50%;background:var(--white);display:block}
.f-head{font-family:"Montserrat",sans-serif;font-weight:700;font-size:12px;top:76px}
.f-list{font-size:11px;line-height:1.6}
.f-row{display:flex;gap:12px;align-items:flex-start;margin-bottom:18px}
.social{display:flex;align-items:center;gap:12px;margin-bottom:14px;font-size:11px}
.social i{width:26px;height:26px;border-radius:50%;background:var(--navy);display:block}
.f-rule{left:134px;top:290px;width:934px;height:1px;background:rgba(255,255,255,.3)}
.copy{left:0;top:328px;width:1200px;text-align:center;font-size:11px}
</style>
</head>
<body>
<div class="page">

  <!-- header -->
  <div class="abs brand"><div class="brand-dot"></div><div class="brand-name">BRONTAVALE<small>ASIA PACIFIC PTY LTD</small></div></div>
  <div class="abs top-mail">
    <svg width="12" height="9" viewBox="0 0 12 9"><rect width="12" height="9" rx="1" fill="#333"/><path d="M0 1l6 4 6-4" stroke="#fff" fill="none"/></svg>
    sales@tallowcreekparts.com.au
  </div>
  <div class="abs btn login">LOGIN</div>
  <div class="abs search">
    <div class="cat">All Categories <svg width="7" height="4"><path d="M0 0h7L3.5 4z" fill="#333"/></svg></div>
    <div class="field">Search Products</div>
    <div class="go"><svg width="14" height="14" viewBox="0 0 14 14"><circle cx="6" cy="6" r="4.5" stroke="#fff" stroke-width="2" fill="none"/><path d="M9.5 9.5L13 13" stroke="#fff" stroke-width="2"/></svg></div>
  </div>
  <div class="abs call">
    <svg width="16" height="26" viewBox="0 0 16 26"><path d="M5 1c-3 1-4 5-4 12s1 11 4 12l3-1-2-7-2 1c-1-3-1-7 0-10l2 1 2-7z" fill="var(--navy)"/></svg>
    <p>Call Us Now on<strong>1300 555 219</strong></p>
  </div>
  <div class="abs nav" style="left:487px">HOME</div>
  <div class="abs nav" style="left:566px">CATEGORIES ▾</div>
  <div class="abs nav" style="left:704px">ABOUT US</div>
  <div class="abs nav" style="left:820px">CONTACT US</div>
  <div class="abs cart">MY CART<br><span>$0.00</span></div>
  <svg class="abs" style="left:1040px;top:118px" width="24" height="28" viewBox="0 0 24 28"><path d="M7 8V5a5 5 0 0110 0v3" stroke="#333" stroke-width="2" fill="none"/><rect x="1" y="8" width="22" height="19" rx="2" fill="#333"/><circle cx="12" cy="18" r="5" fill="var(--sky)"/></svg>

  <!-- hero -->
  <div class="abs hero" role="img" aria-label="Close-up of colourful stripped power cables"></div>
  <div class="abs hero-title">Power Cable</div>
  <div class="abs hero-text">Sed ut perspiciatis unde omnis iste natus error sit voluptatem accusantium doloremque.</div>
  <div class="abs btn hero-btn">Read More</div>
  <div class="abs dots"><i></i><i></i><i class="on"></i><i></i><i></i></div>

  <!-- categories -->
  <h2 class="abs sec-title" style="top:762px">PRODUCT CATEGORIES</h2>
  <p class="abs sec-sub" style="top:806px">The Products we sell</p>
  <div class="abs grid">
    <div class="card"><h3>Black Nylon<span>Flexible Conduit</span></h3><div class="btn">SHOP NOW</div><div class="photo" role="img" aria-label="Coil of black flexible conduit" style="background:radial-gradient(#555,#1a1a1a 60%,var(--card) 72%)"></div></div>
    <div class="card"><h3>Stainless Steel<span>cable ties</span></h3><div class="btn">SHOP NOW</div><div class="photo" role="img" aria-label="Stainless steel cable ties" style="background:linear-gradient(160deg,var(--card),#c9c9c9 50%,var(--card))"></div></div>
    <div class="card"><h3>Nylon<span>cable ties</span></h3><div class="btn">SHOP NOW</div><div class="photo" role="img" aria-label="Bundles of coloured nylon cable ties" style="background:linear-gradient(90deg,#1f3fbf,#222,#e0d8b0,#e66a1a,#3c7a2a,#6a3a1a)"></div></div>
    <div class="card"><h3>EPDM<span>Cold shrink</span></h3><div class="btn">SHOP NOW</div><div class="photo" role="img" aria-label="Black EPDM cold shrink tubes" style="background:linear-gradient(150deg,var(--card),#1c1c1c 50%,var(--card))"></div></div>
    <div class="card"><h3>Earth Bars</h3><div class="btn" style="margin-top:36px">SHOP NOW</div><div class="photo" role="img" aria-label="Metal earth bars" style="background:linear-gradient(160deg,var(--card),#a8a8a8 50%,var(--card))"></div></div>
    <div class="card"><h3>Red / Blue<span>DC cable - Twin</span></h3><div class="btn">SHOP NOW</div><div class="photo" role="img" aria-label="Spool of red and blue twin DC cable" style="background:radial-gradient(#7a2a8a,#3a2a9a 55%,var(--card) 72%)"></div></div>
    <div class="card"><h3>Earth<span>Pits</span></h3><div class="btn">SHOP NOW</div><div class="photo" role="img" aria-label="Earth pit box with grate lid" style="background:linear-gradient(#9a9a9a,#e8dcc4 40%,var(--card))"></div></div>
    <div class="card"><h3>10 and 25 pair<span>phone cable</span></h3><div class="btn">SHOP NOW</div><div class="photo" role="img" aria-label="Multi-pair phone cable with coloured cores" style="background:linear-gradient(150deg,var(--card),#c8ccd4 45%,#d86ab0 70%,var(--card))"></div></div>
  </div>
  <div class="abs btn more">More Categories</div>
  <div class="abs band"></div>

  <!-- newest products -->
  <h2 class="abs sec-title" style="top:1740px">NEWEST PRODUCTS</h2>
  <p class="abs sec-sub" style="top:1784px">Latest Products we sell</p>
  <div class="abs arrow" style="left:0"><svg width="10" height="14"><path d="M8 1L2 7l6 6" stroke="#fff" stroke-width="2.5" fill="none"/></svg></div>
  <div class="abs arrow" style="left:1172px"><svg width="10" height="14"><path d="M2 1l6 6-6 6" stroke="#fff" stroke-width="2.5" fill="none"/></svg></div>
  <div class="abs product" style="left:67px;top:1883px"><div class="photo" role="img" aria-label="Black cable with metal connectors" style="background:radial-gradient(ellipse,#fff 30%,#222 48%,#fff 62%)"></div><p>Remote Elevation Tilt cables</p><div class="price">$ 49.<sup>00</sup></div><div class="btn">ADD TO CART</div></div>
  <div class="abs product" style="left:364px;top:1883px"><div class="photo" role="img" aria-label="Blue network patch cord" style="background:radial-gradient(ellipse,#fff 30%,#1f4fb0 48%,#fff 62%)"></div><p style="margin-top:52px">CAT 6 and CAT 5 patch cords</p><div class="price">$ 49.<sup>00</sup></div><div class="btn">ADD TO CART</div></div>
  <div class="abs product" style="left:660px;top:1883px"><div class="photo" role="img" aria-label="Handheld label printers" style="background:radial-gradient(ellipse,#5a5a5a 25%,#bfbfb0 45%,#fff 65%)"></div><p>Korvel printer and cartridges</p><div class="price">$ 49.<sup>00</sup></div><div class="btn">ADD TO CART</div></div>
  <div class="abs product" style="left:926px;top:1883px"><div class="photo" role="img" aria-label="Red insulator fittings" style="background:radial-gradient(ellipse,#d8202a 30%,#fff 58%)"></div><p>Vantor1014</p><div class="price">$ 49.<sup>00</sup></div><div class="btn">ADD TO CART</div></div>

  <!-- footer -->
  <footer class="abs footer">
    <div class="abs f-brand"><i></i>BRONTAVALE</div>

    <div class="abs f-head" style="left:394px">CONTACT US</div>
    <div class="abs f-list" style="left:394px;top:108px">
      <div class="f-row"><svg width="10" height="14" viewBox="0 0 10 14"><path d="M5 0a5 5 0 015 5c0 4-5 9-5 9S0 9 0 5a5 5 0 015-5z" fill="#fff"/><circle cx="5" cy="5" r="2" fill="var(--sky)"/></svg><span>Victoria : 7-9 Fernhill Way,<br>Kestrel Park, VIC, 3999</span></div>
      <div class="f-row"><svg width="12" height="12" viewBox="0 0 12 12"><path d="M2 0l3 3-1.5 2a8 8 0 003.5 3.5L9 7l3 3-2 2C5 12 0 7 0 2z" fill="#fff"/></svg><span>1300 555 219</span></div>
      <div class="f-row"><svg width="12" height="9" viewBox="0 0 12 9"><rect width="12" height="9" rx="1" fill="#fff"/><path d="M0 1l6 4 6-4" stroke="var(--sky)" fill="none"/></svg><span>sales@tallowcreekparts.com.au</span></div>
    </div>

    <div class="abs f-head" style="left:708px">MENU</div>
    <div class="abs f-list" style="left:708px;top:108px;line-height:1.6">HOME<br>CATEGORIES<br>ABOUT US<br>CONTACT US</div>

    <div class="abs f-head" style="left:939px">CONNECT WITH US</div>
    <div class="abs" style="left:941px;top:110px">
      <div class="social"><i></i>Friendpage</div>
      <div class="social"><i></i>Chirpline</div>
      <div class="social"><i></i>Worknet</div>
    </div>

    <div class="abs f-rule"></div>
    <div class="abs copy">Copyrights @ 2018 All Rights Reserved</div>
  </footer>
</div>
</body>
</html>
```